Wine Importer Needs a Wordpress Template

Our company, Corbanne Cellar Traders Ltd, requires a Wordpress template for our new website location (brastellcask.ie).

We specialise in importing Moldovan wine into Ireland. I have attached a presentation that has background information about the main winery and its wine. I would very much like to see something similar to this in feel and colour. I have also attached our logo which might be useful.

We are very much open to new ideas, so long as the result is something that is clean and easy to use.

Many thanks.
Updates

Project Deadline Extended
Reason: I have extended the deadline by a few days given that I was unable to respond timely to queries. My apologies to all for this. I will be available from now until the new deadline.

Project Deadline Extended

Industry/Entity Type

It Company

```html
<!DOCTYPE html>
<html lang="en">
<head>
<meta charset="utf-8">
<title>Corbanne Cellar Traders Ltd</title>
<link href="https://fonts.googleapis.com/css2?family=Gelasio&family=Sanchez&display=swap" rel="stylesheet">
<style>
  :root {
    --wine: #a20c12;
    --wine-dark: #7a1a1a;
    --brand: #8c5a5a;
    --rule: #f0c2a0;
    --rule-dark: #8a4a3a;
    --ink: #1a1a1a;
    --muted: #8a8a8a;
    --heading: #5a2a22;
    --white: #ffffff;
  }
  * { box-sizing: border-box; margin: 0; padding: 0; }
  html, body { width: 1200px; height: 938px; overflow: hidden; background: var(--white); }
  body { position: relative; font-family: "Sanchez", Georgia, serif; color: var(--ink); }

  .brand { position: absolute; left: 0; width: 1200px; top: 68px; display: flex; justify-content: center; align-items: center; gap: 12px; }
  .brand-dot { width: 26px; height: 26px; border-radius: 50%; border: 2px solid var(--brand); }
  .brand-name { font-size: 26px; color: var(--brand); letter-spacing: 2px; text-transform: uppercase; }

  .main-nav { position: absolute; left: 149px; width: 900px; top: 176px; height: 33px; border-top: 1px solid var(--rule); border-bottom: 1px solid var(--rule); display: flex; justify-content: center; align-items: center; gap: 31px; }
  .main-nav a { font-size: 12.5px; color: var(--ink); text-decoration: none; text-transform: uppercase; }

  .hero { position: absolute; left: 0; top: 232px; width: 1200px; height: 237px; background: linear-gradient(90deg, #b8776a 0%, #d9a99a 25%, #c48f80 50%, #a8685c 75%, #c9998a 100%); }
  .hero-arrow { position: absolute; top: 100px; }
  .hero-arrow.prev { left: 98px; }
  .hero-arrow.next { left: 1092px; }

  .tagline { position: absolute; left: 0; top: 472px; width: 1200px; height: 54px; background: var(--wine); display: flex; justify-content: center; align-items: center; gap: 26px; }
  .tagline h1 { font-family: "Gelasio", Georgia, serif; font-weight: 400; font-size: 29px; color: var(--white); }
  .tagline .line { width: 98px; height: 1px; background: var(--white); }

  .backdrop { position: absolute; left: 0; top: 526px; width: 1200px; height: 412px; background: linear-gradient(180deg, #eeeeee 0%, #f5f5f5 50%, #fafafa 100%); }

  .column { position: absolute; top: 575px; width: 233px; }
  .column h2 { font-size: 12px; font-weight: 400; color: var(--heading); text-transform: uppercase; padding-bottom: 9px; border-bottom: 1px solid var(--rule-dark); }
  .column p { margin-top: 14px; font-size: 11.5px; line-height: 17px; color: var(--muted); }
  .column p a { color: var(--wine); text-decoration: none; }
  .col-newsletter { left: 150px; }
  .col-news { left: 484px; }
  .col-video { left: 817px; }

  .field { position: absolute; left: 151px; width: 230px; height: 20px; background: var(--white); border: 1px solid #ddd; font-size: 11px; color: var(--heading); padding: 3px 7px; }
  .field.name { top: 666px; }
  .field.email { top: 701px; }
  .signup { position: absolute; left: 291px; top: 730px; width: 90px; height: 30px; background: var(--wine); color: var(--white); border-radius: 4px; font-size: 11.5px; display: flex; align-items: center; justify-content: center; }

  .video { position: absolute; left: 817px; top: 670px; width: 219px; height: 141px; background: var(--white); padding: 5px 4px; }
  .video-still { position: relative; width: 100%; height: 100%; background: linear-gradient(135deg, #7d8fb0 0%, #c26a5a 45%, #5e7390 100%); }
  .video-play { position: absolute; left: 69px; top: 31px; }

  .site-footer { position: absolute; left: 149px; width: 900px; top: 867px; height: 33px; border-top: 1px solid #cfcfcf; border-bottom: 1px solid #cfcfcf; display: flex; justify-content: center; align-items: center; gap: 31px; font-size: 11.5px; }
</style>
</head>
<body>
  <header class="brand">
    <span class="brand-dot"></span>
    <span class="brand-name">Corbanne Limited</span>
  </header>

  <nav class="main-nav">
    <a href="#">Home</a>
    <a href="#">About Us</a>
    <a href="#">Our Products</a>
    <a href="#">Latest News</a>
    <a href="#">Contact Us</a>
  </nav>

  <section class="hero" role="img" aria-label="Wine shop interior with shelves of boxed gifts and bottles, tinted red">
    <svg class="hero-arrow prev" width="30" width="30" height="56" viewBox="0 0 30 56"><path d="M28 0 L10 28 L28 56 L14 56 L0 28 L14 0 Z" fill="#fff"/></svg>
    <svg class="hero-arrow next" width="30" height="56" viewBox="0 0 30 56"><path d="M2 0 L20 28 L2 56 L16 56 L30 28 L16 0 Z" fill="#fff"/></svg>
  </section>

  <div class="tagline">
    <span class="line"></span>
    <h1>Explore our world of Super Premium wines...</h1>
    <span class="line"></span>
  </div>

  <div class="backdrop" role="img" aria-label="Faded view of the shop shelves"></div>

  <section class="column col-newsletter">
    <h2>Email Newsletter</h2>
    <p>Sign-up to receive news about exciting products and interesting tastings.</p>
  </section>
  <div class="field name">Name :</div>
  <div class="field email">Email :</div>
  <div class="signup">Sign Up</div>

  <section class="column col-news">
    <h2>News Feed</h2>
    <p>There is always something new at Corbanne. Follow us on <a href="#">Chatterline</a>.</p>
  </section>

  <section class="column col-video">
    <h2>Latest Video</h2>
    <p>Check out videos from our events and travels. Visit us on ClipStream</p>
  </section>
  <div class="video">
    <div class="video-still" role="img" aria-label="Video thumbnail with colourful painted title artwork">
      <svg class="video-play" width="72" height="72" viewBox="0 0 72 72"><circle cx="36" cy="36" r="36" fill="#a20c12" fill-opacity="0.85"/><path d="M29 24 L48 36 L29 48 Z" fill="#fff"/></svg>
    </div>
  </div>

  <footer class="site-footer">
    <span>Legal Disclaimer</span>
    <span>Privacy Policy</span>
    <span>© 2014 Corbanne Cellar Traders Ltd.</span>
  </footer>
</body>
</html>
```